Rtvlegal.com needs a wedsite. Law Office of Bernard T. Whitfield

Bernard T. Whitfield is a criminal law firm that is 5 years old. We have already had all the content written and now just need the website designed. We also just finished our logo design using Pixel Harbor and would like it used in the design of the website.

Industry/Entity Type

Law Firm

Number of Pages Required

5+ page

Requirements
Must have
• I was our new logo to be on the website also. I want Dallas sites as the stock pictures for the website. For example the Grey Stone Hall. I also need to be able to add ClipNest videos. It has to adjust to be seen on computers and also cell phones. I need to be able to have a information sheet for clients to fill out and submit back to me.

```html
<!DOCTYPE html>
<html lang="en">
<head>
<meta charset="utf-8">
<title>Law Office of Bernard T. Whitfield — Dallas Criminal Defense</title>
<link rel="stylesheet" href="https://fonts.googleapis.com/css2?family=Fira+Sans+Condensed:wght@400;500&family=Jost:wght@500&family=Montserrat:wght@400;500;600&display=swap">
<style>
:root{
  --page-dark:#2d3440;
  --white:#ffffff;
  --navy:#0b2a6b;
  --slate:#3d4a5c;
  --nav-text:#4a4f57;
  --body-text:#4b4f55;
  --side-bg:#d4d6d9;
  --caption-bg:rgba(255,255,255,.86);
}
*{margin:0;padding:0;box-sizing:border-box}
html,body{width:1200px;height:1169px;overflow:hidden}
body{background:var(--page-dark);position:relative;font-family:"Montserrat",sans-serif}
.site-header{position:absolute;left:0;top:0;width:1200px;height:155px;background:var(--white)}
.brand{position:absolute;left:90px;top:16px;display:flex;align-items:center;gap:10px}
.brand-mark{width:52px;height:52px;border-radius:50%;background:var(--navy)}
.brand-name{font-family:"Fira Sans Condensed",sans-serif;font-weight:500;font-size:17px;color:var(--navy);width:130px;line-height:1.2}
.main-nav{position:absolute;right:119px;top:50px;text-align:right;font-family:"Fira Sans Condensed",sans-serif;font-size:16px;color:var(--nav-text);line-height:22px}
.main-nav span{margin-left:22px}
.content{position:absolute;left:58px;top:155px;width:1074px;height:917px;background:var(--white)}
.hero{position:absolute;left:0;top:0;width:1074px;height:399px;background:linear-gradient(100deg,#8d959c 0%,#c9ced2 35%,#e6e8ea 55%,#aab3ba 80%,#6f7a84 100%)}
.hero-caption{position:absolute;right:0;top:249px;width:416px;height:144px;background:var(--caption-bg);padding:16px 54px 0 0;text-align:right;font-family:"Jost",sans-serif;font-weight:500;font-size:34px;line-height:38px;color:var(--navy)}
.service{position:absolute;top:435px;width:218px;text-align:center}
.service-photo{width:218px;height:131px;background:linear-gradient(135deg,#c9b8a8,#8a7a70)}
.service-label{margin-top:14px;font-weight:600;font-size:18px;letter-spacing:1px;line-height:26px;color:var(--slate)}
.intro{position:absolute;left:68px;top:672px;width:712px;color:var(--body-text)}
.intro h2{font-weight:600;font-size:26px;letter-spacing:1px;color:var(--navy);margin-bottom:22px}
.intro h3{font-weight:500;font-size:16px;color:#555a60;line-height:18px}
.intro p{font-size:12.4px;line-height:15.8px;letter-spacing:.2px}
.rights{position:absolute;left:815px;top:429px;width:235px;height:437px;background:var(--side-bg);padding:26px 14px 0 18px;color:#4b5058}
.rights h2{font-weight:500;font-size:17.5px;line-height:21px;margin-bottom:4px}
.rights p{font-size:12.6px;line-height:21.5px;letter-spacing:.3px}
.site-footer{position:absolute;left:103px;top:1094px;font-family:Arial,sans-serif;font-size:13px;color:var(--white);line-height:21px}
.social{position:absolute;right:64px;top:1102px;display:flex;gap:14px;font-family:"Fira Sans Condensed",sans-serif;font-size:14px;color:#b9bec6}
</style>
</head>
<body>
<header class="site-header">
  <div class="brand">
    <span class="brand-mark"></span>
    <span class="brand-name">Law Office of Bernard T. Whitfield</span>
  </div>
  <nav class="main-nav">
    <div><span>Attorney Profile</span><span>How We Can Help</span><span>Murder &amp; Other Homicide Offenses</span><span>Expungements &amp; Non-Disclosures</span></div>
    <div><span>Sexual Offenses</span><span>Early Probation Release</span><span>Probation Violations</span><span>Other Violent Offenses</span><span>DWI, DUI</span><span style="margin-left:12px">Drug Offenses</span></div>
  </nav>
</header>

<main class="content">
  <section class="hero" role="img" aria-label="Attorneys reviewing a case file with a client at a conference table, Dallas skyline through the window">
    <h1 class="hero-caption">Dallas Defense Law Firm Advocates for Your Rights</h1>
  </section>

  <div class="service" style="left:42px">
    <div class="service-photo" role="img" aria-label="Photo representing sexual offense defense"></div>
    <div class="service-label">SEXUAL OFFENSES</div>
  </div>
  <div class="service" style="left:295px">
    <div class="service-photo" role="img" aria-label="Photo of handcuffed hands"></div>
    <div class="service-label">EARLY PROBATION<br>RELEASE</div>
  </div>
  <div class="service" style="left:550px">
    <div class="service-photo" role="img" aria-label="Photo of a man holding up a red card" style="background:linear-gradient(135deg,#b3b5b8,#6c6f74)"></div>
    <div class="service-label">PROBATION<br>VIOLATIONS</div>
  </div>

  <section class="intro">
    <h2>HOW WE CAN HELP</h2>
    <h3>Dallas Defense Law Firm Advocates for Your Rights</h3>
    <p>The Law Office of Bernard T. Whitfield was founded on the principle embedded in the U.S. Constitution, which states not only that all men are created equal, but that everyone is innocent until proven guilty. Yet, we recognize the criminal process often slants toward the prosecution of individuals instead of the pursuit of justice. Our goal is to balance the scales through zealous advocacy.</p>
    <p>We presume each case will go to trial. Our extensive preparation for trial gives us an edge during plea negotiations because prosecutors know we are ready and willing to bring the case in front of a jury.</p>
    <p>If you have been charged with a crime, our lawyers are available 24/7 to defend your rights during the investigation and assist you with jail release. Our experienced attorneys give you the individualized attention and aggressive representation you deserve.</p>
  </section>

  <aside class="rights">
    <h2>Your Fifth Amendment Rights</h2>
    <p>Being arrested for a crime is a frightening experience. Your first inclination may be to tell investigators what they want to hear or to try to talk your way out it. You may at first believe that allowing law enforcement to search your home, vehicle or belongings will make you appear less guilty. However, the most effective line of defense you can take is to remain silent and call your lawyer. You are guaranteed these rights under the Fifth Amendment.</p>
  </aside>
</main>

<footer class="site-footer">
  <div>© 2015 btw</div>
  <div>Home - Site Map – FAQ – Privacy Policy – Terms of Use – Contact Us</div>
</footer>
<div class="social"><span>Friendly</span><span>Chirper</span><span>Feedline</span><span>Circleup</span></div>
</body>
</html>
```